MOSLEN Environmental needs an upgrade to its current business cards design

We need an upgrade to our current business cards design, where the MOSLEN acronym is included, as possible and not being overloaded.
MOSLEN Environmental is an Environmental Consultancy Firm based in Sydney.
We would like to see creative designs different from the standard type of business cards (for example, rounded edges, different to standard size of common business cards.

Target Market(s)

industrial companies (oil & gas, petrochemical, mining, insolvency, finance and manufacturing), developers, architect firms, law firms.

Industry/Entity Type

Business

Contact Information for Business Card

logos (brand and acronym), if they don't appear overloaded.
name
role
name of company (MOSLEN Environmental),
address (Level 3, Suite 3C, 47-49 Dorrigan Lane, Wexmoor, NSW, 2188) landline (02 7314 2986)
mobile (staff member)
email (staff member) and
website (www.moslengreen.example).
Include: Contaminated Land, Site Remediation, Groundwater Assessment, Health and Ecological Risk Assessments, Acid Sulfate Soils, Waste Classification.

Font styles to use
Serif
Sans Serif

Requirements
Must have
• A creative design different to the standard type of business cards.
Nice to have
• Rounded edges
• Different size of business cards rather than the standard size.
Should not have
• Preferable not to use white colour background, unless it is required from a creative design proposed.
• Not an overloaded design.
• Avoid black colours

```html
<!DOCTYPE html>
<html lang="en">
<head>
<meta charset="utf-8">
<title>MOSLEN Environmental – Business Card</title>
<link rel="stylesheet" href="https://fonts.googleapis.com/css2?family=Montserrat:wght@600;800&family=Roboto+Slab:wght@400;500&display=swap">
<style>
  :root {
    --stage: #2b2d30;
    --card-dark: #161616;
    --brand-green: #6ab43e;
    --green-light: #7cc04a;
    --stripe: #ffffff;
    --ink-light: #f2f2f2;
    --ink-muted: #cfcfcf;
  }
  * { margin: 0; padding: 0; box-sizing: border-box; }
  html, body { width: 1200px; height: 900px; overflow: hidden; background: var(--stage); }
  .stage {
    width: 1200px; height: 900px;
    display: flex; flex-direction: column; align-items: center; justify-content: center; gap: 48px;
  }
  .card {
    position: relative; width: 660px; height: 377px;
    border-radius: 22px; overflow: hidden;
    box-shadow: 0 14px 30px rgba(0,0,0,.45);
  }
  .card-shapes { position: absolute; inset: 0; }

  /* Front */
  .card--front { background: linear-gradient(135deg, var(--green-light), var(--brand-green)); }
  .brand-mark {
    position: absolute; font-family: "Montserrat", sans-serif; font-weight: 800;
    line-height: .95; letter-spacing: .02em; text-transform: uppercase;
  }
  .card--front .brand-mark { left: 34px; top: 26px; color: var(--ink-light); }
  .brand-mark .brand-name { display: block; font-size: 50px; }
  .brand-mark .brand-sub { display: block; font-size: 13px; letter-spacing: .32em; margin-top: 6px; }
  .address {
    position: absolute; left: 92px; top: 144px;
    transform: rotate(10.5deg); transform-origin: left top;
    font-family: "Roboto Slab", serif; font-size: 13px; color: var(--ink-light);
    display: flex; align-items: center; gap: 8px; white-space: nowrap;
  }
  .person { position: absolute; left: 30px; top: 214px; font-family: "Montserrat", sans-serif; }
  .person-name { font-size: 24px; font-weight: 600; letter-spacing: .03em; }
  .person-name .first { color: var(--brand-green); }
  .person-name .last { color: var(--ink-light); }
  .person-role { font-size: 12px; color: var(--ink-muted); margin-top: 4px; }
  .contact-list {
    position: absolute; left: 250px; top: 268px; list-style: none;
    font-family: "Roboto Slab", serif; font-size: 14px; color: var(--ink-light);
  }
  .contact-list li { display: flex; align-items: center; gap: 12px; height: 22px; }
  .contact-list svg { width: 14px; height: 14px; flex: none; }

  /* Back */
  .card--back { background: var(--card-dark); }
  .card--back .brand-mark { left: 0; right: 0; top: 104px; text-align: center; color: var(--brand-green); }
  .card--back .brand-name { font-size: 74px; }
  .card--back .brand-sub { font-size: 16px; letter-spacing: .4em; margin-top: 8px; }
  .services {
    position: absolute; left: 0; right: 0; top: 250px; text-align: center;
    font-family: "Roboto Slab", serif; font-size: 13px; letter-spacing: .06em;
    color: var(--brand-green); line-height: 1.7;
  }
</style>
</head>
<body>
<main class="stage">
  <section class="card card--front" aria-label="Business card front">
    <svg class="card-shapes" viewBox="0 0 660 377" preserveAspectRatio="none" aria-hidden="true">
      <polygon points="0,160 560,262 518,377 0,377" fill="var(--stripe)"/>
      <polygon points="0,168 548,270 508,377 0,377" fill="var(--card-dark)"/>
    </svg>
    <div class="brand-mark"><span class="brand-name">Moslen</span><span class="brand-sub">Environmental</span></div>
    <p class="address">
      <svg width="14" height="14" viewBox="0 0 24 24" fill="none" stroke="currentColor" stroke-width="2"><path d="M12 22s7-7 7-12a7 7 0 0 0-14 0c0 5 7 12 7 12z"/><circle cx="12" cy="10" r="2.5"/></svg>
      Address: Level 3, Suite 3C, 47-49 Dorrigan Lane, Wexmoor, NSW, 2188
    </p>
    <div class="person">
      <p class="person-name"><span class="first">CORIN</span> <span class="last">VALE</span></p>
      <p class="person-role">Founder &amp; CEO</p>
    </div>
    <ul class="contact-list">
      <li><svg viewBox="0 0 24 24" fill="currentColor"><path d="M6.6 10.8a15 15 0 0 0 6.6 6.6l2.2-2.2c.3-.3.7-.4 1-.2 1.1.4 2.3.6 3.6.6.6 0 1 .4 1 1V20c0 .6-.4 1-1 1A17 17 0 0 1 3 4c0-.6.4-1 1-1h3.5c.6 0 1 .4 1 1 0 1.3.2 2.5.6 3.6.1.3 0 .7-.2 1z"/></svg>02 7314 2986</li>
      <li><svg viewBox="0 0 24 24" fill="none" stroke="currentColor" stroke-width="2"><rect x="7" y="2" width="10" height="20" rx="2"/><line x1="11" y1="18" x2="13" y2="18"/></svg>+01 0263 557 819</li>
      <li><svg viewBox="0 0 24 24" fill="none" stroke="currentColor" stroke-width="2"><rect x="3" y="5" width="18" height="14" rx="1"/><path d="M3 6l9 7 9-7"/></svg>info@corinvale.example</li>
      <li><svg viewBox="0 0 24 24" fill="none" stroke="currentColor" stroke-width="2"><circle cx="12" cy="12" r="9"/><path d="M3 12h18M12 3c3 3 3 15 0 18M12 3c-3 3-3 15 0 18"/></svg>www.moslengreen.example</li>
    </ul>
  </section>

  <section class="card card--back" aria-label="Business card back">
    <div class="brand-mark"><span class="brand-name">Moslen</span><span class="brand-sub">Environmental</span></div>
    <p class="services">Technical / Remediation / Assessment<br>Contaminated / Environments</p>
  </section>
</main>
</body>
</html>
```